Presentation Folder, Business Card, Letterhead and Envelope design

We are a dental clinic that will open in August and we are looking for a professional graphic designer to create our Business Card, Presentation Folder, Letterhead, Notepad and envelopes.

The brand LumaGrin must reflect a sense of quality and sophistication, marketed for middle-class consumers.
Our preference is for quality and refined materials, where less is more.
Attached the logo

```html
<!DOCTYPE html>
<html lang="en">
<head>
<meta charset="utf-8">
<title>LumaGrin — Business Card</title>
<link rel="stylesheet" href="https://fonts.googleapis.com/css2?family=Jost:wght@400&family=Montserrat:wght@300;600&display=swap">
<style>
  :root {
    --slate: #575958;
    --wine: #6a0f10;
    --paper: #ffffff;
    --backdrop: #eeeeee;
    --ink-light: #ffffff;
    --ink-dark: #575958;
  }
  * { margin: 0; padding: 0; box-sizing: border-box; }
  html, body { width: 1159px; height: 1200px; overflow: hidden; background: var(--backdrop); }
  .sheet { position: relative; width: 1159px; height: 1200px; }
  .card {
    position: absolute; left: 100px; width: 960px; height: 550px;
    background: var(--paper); overflow: hidden;
    box-shadow: 0 4px 14px rgba(0,0,0,0.18);
  }
  .card--front { top: 36px; }
  .card--back { top: 614px; }
  .card__shapes { position: absolute; inset: 0; width: 100%; height: 100%; }
  .brand { position: absolute; display: flex; align-items: center; }
  .brand__dot { display: block; border-radius: 50%; }
  .brand__name {
    font-family: "Montserrat", sans-serif; font-weight: 600;
    line-height: 1; white-space: nowrap; letter-spacing: 0;
  }
  .card--front .brand { left: 73px; top: 88px; gap: 16px; }
  .card--front .brand__dot { width: 40px; height: 40px; background: var(--ink-light); }
  .card--front .brand__name { font-size: 52px; color: var(--ink-light); }
  .card--back .brand { left: 330px; top: 232px; gap: 16px; }
  .card--back .brand__dot { width: 42px; height: 42px; background: var(--slate); }
  .card--back .brand__name { font-size: 54px; color: var(--ink-dark); }
  .holder { position: absolute; left: 73px; top: 232px; color: var(--ink-light); }
  .holder__name { font-family: "Montserrat", sans-serif; font-weight: 600; font-size: 37px; line-height: 1.1; }
  .holder__role { font-family: "Montserrat", sans-serif; font-weight: 300; font-size: 24px; line-height: 1.1; }
  .contacts {
    position: absolute; right: 40px; top: 374px; list-style: none;
    font-family: "Jost", sans-serif; font-size: 23px; color: var(--ink-light);
  }
  .contacts__item { display: flex; justify-content: flex-end; align-items: center; gap: 10px; height: 34px; }
  .contacts__icon { width: 18px; height: 18px; fill: none; stroke: var(--ink-light); stroke-width: 1.8; stroke-linecap: round; stroke-linejoin: round; }
</style>
</head>
<body>
<main class="sheet">
  <section class="card card--front" aria-label="Business card front">
    <svg class="card__shapes" viewBox="0 0 855 490" preserveAspectRatio="none" aria-hidden="true">
      <path d="M0 0 H855 V85 C700 255 360 322 0 327 Z" fill="var(--slate)"/>
      <path d="M30 490 C400 440 700 300 855 85 V490 Z" fill="var(--wine)"/>
    </svg>
    <div class="brand">
      <span class="brand__dot" aria-hidden="true"></span>
      <span class="brand__name">LumaGrin</span>
    </div>
    <div class="holder">
      <p class="holder__name">Name Surname</p>
      <p class="holder__role">(Director)</p>
    </div>
    <ul class="contacts">
      <li class="contacts__item">+00 321 654 987
        <svg class="contacts__icon" viewBox="0 0 20 20" aria-hidden="true"><path d="M4 2 L7 2 L8.5 6 L6.5 7.5 C7.5 10 10 12.5 12.5 13.5 L14 11.5 L18 13 V16 C18 17 17 18 16 18 C8.5 17.5 2.5 11.5 2 4 C2 3 3 2 4 2 Z"/></svg>
      </li>
      <li class="contacts__item">hello@lumagrin.com
        <svg class="contacts__icon" viewBox="0 0 20 20" aria-hidden="true"><rect x="2" y="4" width="16" height="12" rx="1"/><path d="M2 5 L10 11 L18 5"/></svg>
      </li>
      <li class="contacts__item">www.lumagrin.com
        <svg class="contacts__icon" viewBox="0 0 20 20" aria-hidden="true"><path d="M8.5 11.5 L11.5 8.5"/><path d="M9 6 L11 4 A3 3 0 0 1 16 9 L14 11"/><path d="M11 14 L9 16 A3 3 0 0 1 4 11 L6 9"/></svg>
      </li>
      <li class="contacts__item">Harbour Lane 7-4B, London
        <svg class="contacts__icon" viewBox="0 0 20 20" aria-hidden="true"><path d="M10 18 C10 18 4 12 4 8 A6 6 0 0 1 16 8 C16 12 10 18 10 18 Z"/><circle cx="10" cy="8" r="2"/></svg>
      </li>
    </ul>
  </section>

  <section class="card card--back" aria-label="Business card back">
    <svg class="card__shapes" viewBox="0 0 855 490" preserveAspectRatio="none" aria-hidden="true">
      <path d="M0 85 C150 330 500 468 855 490 H0 Z" fill="var(--wine)"/>
    </svg>
    <div class="brand">
      <span class="brand__dot" aria-hidden="true"></span>
      <span class="brand__name">LumaGrin</span>
    </div>
  </section>
</main>
</body>
</html>
```